Property Investment eBook Cover

I am a long established Australian property investment adviser, analyst and consultant who is now in semi-retired mode and have re-branded to reflect a more casual and personal approach to advising my property investor clients. I am writing a 'revised edition' to a book written in partnership with my father 20 years ago and need an eBook Cover for this new edition. The eBook will be uploaded to all the regular Australian providers (Larkfield Reader, Quince Folio, Tavi, Pagemarten)

The 3 key elements in the book cover are:

Title: The Harvest Engine of Land. The word 'Property' should be larger and more prominent. eg "The Wealth Power of" could be 1/3 the size of "Property" - with both justified left

Edition: Sydney 2021. "Sydney 2021" should be the focus and dominant imagery of the eBook cover and more prominent than the Title or Author

Author: Colin Marsh, The Housing Ledger Guide. The word "Author" should not appear. "The Housing Ledger Guide" should appear underneath Colin Marsh and justified to Colin Marsh, therefore a smaller font.

The cover should be simple, but eye-catching. No property images, more of an abstract background, than a background with an image. Our preferred colour palette is more blues/greens. Prefer SerifFonts

Copy of book published 20 years ago attached for reference only

```html
<!DOCTYPE html>
<html lang="en">
<head>
<meta charset="utf-8">
<title>The Harvest Engine of Land — Sydney 2021 Edition</title>
<link rel="stylesheet" href="https://fonts.googleapis.com/css2?family=Cinzel:wght@400;500&family=Open+Sans:wght@700&display=swap">
<style>
  :root {
    --backdrop: #e6e6e6;
    --cover-base: #4f8570;
    --cover-deep: #3f705d;
    --art-light: #8fd2b8;
    --art-mid: #5e9c84;
    --title-white: #f4f7f5;
    --title-green: #16e34c;
    --seal-light: #6f8cf0;
    --seal-dark: #3b55cf;
    --seal-rim: #2c43b3;
    --seal-text: #eef0ff;
    --rule: #d7e6df;
  }
  * { box-sizing: border-box; margin: 0; padding: 0; }
  html, body { width: 1200px; height: 800px; overflow: hidden; }
  body { background: var(--backdrop); position: relative; }

  .cover {
    position: absolute;
    left: 350px; top: 25px;
    width: 500px; height: 750px;
    background: linear-gradient(180deg, var(--cover-base) 0%, var(--cover-base) 70%, var(--cover-deep) 100%);
    overflow: hidden;
  }
  .cover-art {
    position: absolute; left: 0; top: 0;
    width: 500px; height: 470px;
    background:
      radial-gradient(ellipse 60% 55% at 45% 35%, var(--art-light) 0%, rgba(143,210,184,0) 70%),
      linear-gradient(180deg, var(--art-mid) 0%, var(--cover-base) 100%);
    clip-path: polygon(0 0, 100% 0, 100% 55%, 48% 100%, 0 50%);
  }

  .title {
    position: absolute; left: 41px; top: 384px;
    font-family: "Cinzel", serif;
    color: var(--title-white);
  }
  .title-lead {
    display: block;
    font-size: 40px; line-height: 46px; font-weight: 400;
  }
  .title-key {
    display: block;
    margin-top: 6px;
    font-size: 88px; line-height: 80px; font-weight: 400;
    color: var(--title-green);
  }

  .tagline {
    position: absolute; left: 41px; top: 641px;
    font-family: "Open Sans", sans-serif;
    font-weight: 700; font-size: 16px; letter-spacing: 0.1px;
    color: var(--title-white);
  }

  .seal {
    position: absolute; left: 208px; top: 375px;
    width: 192px; height: 192px;
  }
  .seal-text {
    position: absolute; left: 208px; top: 375px;
    width: 192px; height: 192px;
    display: flex; flex-direction: column; align-items: center; justify-content: center;
    font-family: "Cinzel", serif; font-size: 27px; line-height: 33px;
    color: var(--seal-text); text-align: center;
  }

  .byline {
    position: absolute; left: 0; top: 700px; width: 500px;
    display: flex; align-items: center; gap: 6px;
    font-family: "Cinzel", serif; color: var(--title-white);
  }
  .byline-rule { flex: 1; height: 1px; background: var(--rule); }
  .byline-names { text-align: center; }
  .author-name { display: block; font-size: 19px; line-height: 22px; }
  .author-role { display: block; font-size: 11px; line-height: 18px; }
  .byline-names { position: relative; top: 8px; }
</style>
</head>
<body>
  <main class="cover">
    <div class="cover-art" role="img" aria-label="Abstract cascade of teal cubes stacked in columns, seen from below"></div>

    <h1 class="title">
      <span class="title-lead">The</span>
      <span class="title-lead">Harvest</span>
      <span class="title-lead">Engine</span>
      <span class="title-lead">of</span>
      <span class="title-key">Land</span>
    </h1>

    <svg class="seal" viewBox="0 0 192 192" aria-hidden="true">
      <defs>
        <radialGradient id="sealFill" cx="45%" cy="40%" r="65%">
          <stop offset="0%" stop-color="var(--seal-light)"/>
          <stop offset="100%" stop-color="var(--seal-dark)"/>
        </radialGradient>
      </defs>
      <circle cx="96" cy="96" r="90" fill="var(--seal-rim)"/>
      <circle cx="96" cy="96" r="84" fill="url(#sealFill)"/>
      <circle cx="96" cy="96" r="78" fill="none" stroke="var(--seal-light)" stroke-width="1.5" opacity="0.6"/>
    </svg>
    <div class="seal-text">
      <span>Edition:</span>
      <span>Sydney</span>
      <span>2021</span>
    </div>

    <p class="tagline">YOU CAN BE A&nbsp; PROPERTY MULTI - MILLIONAIRE</p>

    <div class="byline">
      <span class="byline-rule"></span>
      <div class="byline-names">
        <span class="author-name">Colin Marsh</span>
        <span class="author-role">The Housing Ledger Guide</span>
      </div>
      <span class="byline-rule"></span>
    </div>
  </main>
</body>
</html>
```